Transportation website

I need website for my company, its gonna be transportation and logistics website, information and address, contact form , service, about

```html
<!DOCTYPE html>
<html lang="en">
<head>
<meta charset="utf-8">
<title>Harlow Freight</title>
<link href="https://fonts.googleapis.com/css2?family=Montserrat:wght@400;500;600;700&family=Open+Sans:wght@400;600&display=swap" rel="stylesheet">
<style>
:root{
  --navy:#1f1f66;
  --navy-deep:#232370;
  --sky:#1ba6ea;
  --white:#ffffff;
  --text:#555a66;
  --star:#e8541c;
}
*{box-sizing:border-box;margin:0;padding:0}
html,body{width:1200px;height:3220px;overflow:hidden;background:var(--white)}
body{position:relative;font-family:"Open Sans",Arial,sans-serif;color:var(--text)}
.abs{position:absolute}
h1,h2,h3,h4,.btn,.brand,.nav a,.submit{font-family:"Montserrat",Arial,sans-serif}

/* welcome background sits under the hero edge */
.welcome{left:0;top:640px;width:1200px;height:584px;background:linear-gradient(180deg,#f7f8fa 0%,#f2f3f6 55%,#eceef2 100%)}

/* header + hero */
.hero{left:0;top:0;width:1200px;height:770px;overflow:hidden}
.hero-photo{position:absolute;inset:0;background:linear-gradient(180deg,#1d2a6e 0%,#2a3f8f 28%,#5e5a8c 46%,#c9763e 60%,#ee8a2c 68%,#3a4270 84%,#1c2758 100%)}
.topbar{position:absolute;left:0;top:0;width:1200px;height:97px;background:rgba(20,24,70,.55)}
.brand{position:absolute;left:112px;top:27px;font-size:31px;font-weight:500;color:var(--white)}
.nav{position:absolute;top:37px;left:600px}
.nav a{position:absolute;font-size:14px;color:var(--white);text-decoration:none;white-space:nowrap}
.hero-copy{left:682px;top:238px;width:420px;color:var(--white)}
.hero-copy h1{font-size:38px;font-weight:700;margin-bottom:16px}
.hero-copy p{font-size:13.5px;line-height:30px;font-weight:600}
.btn{display:inline-block;text-align:center;font-weight:600;color:var(--white);border-radius:30px;text-decoration:none}
.hero-btn{left:682px;top:415px;width:136px;height:48px;line-height:48px;background:var(--navy);font-size:15px}
.hero-edge{left:0;top:630px;width:1200px;height:150px}

.title{width:1200px;text-align:center;font-size:37px;font-weight:700;color:var(--navy)}
.title span{color:var(--sky)}
.rule{left:568px;width:64px;height:2px;background:var(--sky)}
.welcome-text{left:245px;top:910px;width:710px;text-align:center;font-size:13.5px;line-height:29px}
.quote-btn{left:500px;top:1093px;width:202px;height:56px;line-height:56px;background:var(--navy);font-size:19px}

/* services */
.card{top:1360px;width:314px;height:412px}
.card-photo{height:240px;background:linear-gradient(180deg,#c98a5a 0%,#6f7fa0 45%,#34455f 100%)}
.card-body{height:172px;background:var(--navy);color:var(--white);text-align:center;padding-top:30px}
.card.is-featured .card-body{background:var(--sky)}
.card-body h3{font-size:19px;font-weight:500;margin-bottom:14px;letter-spacing:.3px}
.card-body p{font-size:11.5px;line-height:24px;padding:0 26px}

/* why */
.why{left:0;top:1830px;width:1200px;height:422px;background:linear-gradient(100deg,#5b5f86 0%,#6d6f90 35%,#8a8aa2 60%,#3c4f74 80%,#2c3e62 100%)}
.why-title{left:112px;top:1905px;font-size:44px;font-weight:500;color:var(--white)}
.why-text{left:112px;top:1984px;width:520px;font-size:13.5px;line-height:33px;color:var(--white);font-weight:600}
.why-btn{left:113px;top:2119px;width:165px;height:52px;line-height:52px;background:var(--sky);font-size:15px}

/* testimonials */
.person{width:320px;text-align:center;top:2415px}
.avatar{width:165px;height:165px;border-radius:50%;margin:0 auto;background:radial-gradient(circle at 50% 40%,#b58a6e 0%,#6f5648 60%,#3a3a3a 100%)}
.stars{margin-top:12px;height:16px;display:flex;justify-content:center}
.person h4{font-size:19px;font-weight:500;color:#222;margin-top:8px;letter-spacing:.3px}
.person p{font-size:11.5px;line-height:26px;margin-top:8px;padding:0 30px}

/* footer */
.footer{left:0;top:2808px;width:1200px;height:412px;background:var(--navy-deep)}
.foot-head{top:2848px;color:var(--white);font-size:21px;font-weight:500;letter-spacing:.3px}
.links{left:198px;top:2886px;list-style:none;font-size:12.5px;color:var(--white)}
.links li{height:30px;line-height:30px;padding-left:38px;position:relative}
.links li::before{content:"»";position:absolute;left:10px}
.addr{left:505px;top:2893px;font-size:12.5px;line-height:18px;color:var(--white)}
.field{left:770px;width:283px;background:var(--white);color:#555;font-size:12px;padding:8px 10px}
.submit{left:770px;top:3076px;width:90px;height:32px;line-height:32px;background:var(--sky);color:var(--white);font-size:12px;text-align:center}
.social{left:196px;top:3063px;display:flex;gap:7px}
.social span{width:36px;height:36px;border:2px solid var(--white);border-radius:50%}
.copy{left:0;top:3163px;width:1200px;text-align:center;font-size:12px;color:var(--white)}
</style>
</head>
<body>

<section class="abs welcome" role="img" aria-label="Faint background of shipping containers and an aircraft"></section>

<section class="abs hero">
  <div class="hero-photo" role="img" aria-label="Photo of a container ship at a port at sunset, with a plane overhead"></div>
  <header class="topbar">
    <div class="brand">Harlow Freight</div>
    <nav class="nav">
      <a style="left:0;color:var(--sky)">Home</a>
      <a style="left:95px">About Us</a>
      <a style="left:210px">Services</a>
      <a style="left:320px">News</a>
      <a style="left:412px">Contact Us</a>
    </nav>
  </header>
</section>

<div class="abs hero-copy">
  <h1>Harlow Freight</h1>
  <p>Sed ut perspiciatis unde omnis iste natus error sit voluptatem accusantium doloremque laudantium, totam rem aperiam, eaque vitae dicta sunt explicabo.</p>
</div>
<a class="abs btn hero-btn">Read More</a>

<svg class="abs hero-edge" viewBox="0 0 1200 150" width="1200" height="150" aria-hidden="true">
  <polygon points="0,0 600,132 1200,8 1200,150 0,150" fill="#f7f8fa"/>
  <polyline points="0,0 600,132 1200,8" fill="none" stroke="#1ba6ea" stroke-width="7"/>
</svg>

<h2 class="abs title" style="left:0;top:818px">Welcome to <span>Harlow Freight</span></h2>
<div class="abs rule" style="top:884px"></div>
<p class="abs welcome-text">Sed ut perspiciatis unde omnis iste natus error sit voluptatem accusantium doloremque laudantium, totam rem aperiam, eaque ipsa quae ab illo inventore veritatis et quasi architecto beatae vitae dicta sunt explicabo. Nemo enim ipsam voluptatem quia voluptas sit aspernatur aut odit aut fugit, sed quia consequuntur magni dolores eos qui ratione voluptatem sequi nesciunt. Neque porro quisquam est, qui dolorem ipsum quia dolor sit amet, consectetur, adipisci velit, sed quia non numquam eius modi</p>
<a class="abs btn quote-btn">Get A Quote</a>

<h2 class="abs title" style="left:0;top:1263px">Our <span>Services</span></h2>
<div class="abs rule" style="top:1328px"></div>

<article class="abs card" style="left:113px">
  <div class="card-photo" role="img" aria-label="Photo of a container ship docked under port cranes"></div>
  <div class="card-body"><h3>SED UT PERSPICIATIS</h3><p>Sed ut perspiciatis unde omnis iste natus error sit voluptatem accusantium doloremque laudantium, beatae vitae dicta sunt explicabo.</p></div>
</article>
<article class="abs card is-featured" style="left:443px">
  <div class="card-photo" role="img" aria-label="Photo of a plane, cargo ship and truck at dusk"></div>
  <div class="card-body"><h3>SED UT PERSPICIATIS</h3><p>Sed ut perspiciatis unde omnis iste natus error sit voluptatem accusantium doloremque laudantium, beatae vitae dicta sunt explicabo.</p></div>
</article>
<article class="abs card" style="left:774px">
  <div class="card-photo" role="img" aria-label="Aerial photo of a container terminal at sunset"></div>
  <div class="card-body"><h3>SED UT PERSPICIATIS</h3><p>Sed ut perspiciatis unde omnis iste natus error sit voluptatem accusantium doloremque laudantium, beatae vitae dicta sunt explicabo.</p></div>
</article>

<section class="abs why" role="img" aria-label="Photo of a container ship beside harbour cranes on calm water"></section>
<h2 class="abs why-title">Why Choose Us</h2>
<p class="abs why-text">Sed ut perspiciatis unde omnis iste natus error sit voluptatem accusantium dolorem que laudantium, totam rem aperiam, eaque ipsa quae ab illo inven quasi architecto beatae vitae dicta explicabo.</p>
<a class="abs btn why-btn">READ MORE</a>

<h2 class="abs title" style="left:0;top:2294px">Our <span>Testimonials</span></h2>
<div class="abs rule" style="top:2361px"></div>

<svg width="0" height="0" style="position:absolute" aria-hidden="true"><defs><polygon id="star" points="7,0 9,5 14,5 10,8.5 11.5,14 7,10.5 2.5,14 4,8.5 0,5 5,5" fill="#e8541c"/></defs></svg>

<div class="abs person" style="left:105px">
  <div class="avatar" role="img" aria-label="Portrait photo of a client"></div>
  <div class="stars"><svg width="78" height="14" viewBox="0 0 78 14"><use href="#star"/><use href="#star" x="16"/><use href="#star" x="32"/><use href="#star" x="48"/><use href="#star" x="64"/></svg></div>
  <h4>JHON SMITH</h4>
  <p>Sed ut perspiciatis unde omnis iste natus error sit voluptatem accusantium doloremque laudant ium, totam rem aperiam, eaque ipsa quae ab vitae dicta sunt explicabo.</p>
</div>
<div class="abs person" style="left:437px">
  <div class="avatar" role="img" aria-label="Portrait photo of a client"></div>
  <div class="stars"><svg width="78" height="14" viewBox="0 0 78 14"><use href="#star"/><use href="#star" x="16"/><use href="#star" x="32"/><use href="#star" x="48"/><use href="#star" x="64"/></svg></div>
  <h4>JHON SMITH</h4>
  <p>Sed ut perspiciatis unde omnis iste natus error sit voluptatem accusantium doloremque laudant ium, totam rem aperiam, eaque ipsa quae ab vitae dicta sunt explicabo.</p>
</div>
<div class="abs person" style="left:768px">
  <div class="avatar" role="img" aria-label="Portrait photo of a client"></div>
  <div class="stars"><svg width="78" height="14" viewBox="0 0 78 14"><use href="#star"/><use href="#star" x="16"/><use href="#star" x="32"/><use href="#star" x="48"/><use href="#star" x="64"/></svg></div>
  <h4>JHON SMITH</h4>
  <p>Sed ut perspiciatis unde omnis iste natus error sit voluptatem accusantium doloremque laudant ium, totam rem aperiam, eaque ipsa quae ab vitae dicta sunt explicabo.</p>
</div>

<footer class="abs footer"></footer>
<h4 class="abs foot-head" style="left:198px">QUICK LINKS</h4>
<ul class="abs links">
  <li>Home</li><li>About Us</li><li>Services</li><li>News</li><li>Contact Us</li>
</ul>
<div class="abs social"><span></span><span></span><span></span><span></span><span></span></div>

<h4 class="abs foot-head" style="left:505px">ADDRESS</h4>
<div class="abs addr">
  ADDRESS<br>113 S. Lorem Ipsum Dummy<br>Lorem Ipsum<br><br>PHONE<br>000-555-0148<br><br>EMAIL<br>info@harlowfreight.com
</div>

<h4 class="abs foot-head" style="left:770px">CONTACT FORM</h4>
<div class="abs field" style="top:2895px;height:36px">Name :</div>
<div class="abs field" style="top:2935px;height:36px">Email :</div>
<div class="abs field" style="top:2975px;height:36px">Subject :</div>
<div class="abs field" style="top:3015px;height:50px">Message :</div>
<div class="abs submit">SUBMIT</div>

<p class="abs copy">© Copyright 2019 Harlow Freight.All right reserved</p>

</body>
</html>
```